Looking for a clean, modern, and professional business card design that reflects Valtrim Systems

The design should include the company logo, contact details, and align with our brand identity. Please use a sophisticated and minimalist style, incorporating [specific colors, if applicable]. Creativity is welcome, but the card must maintain a polished and professional appearance.

Details to Include:

Name: Gavin Trelowe
Title: VP Sales / Operations
Company: Valtrim Systems
Phone: 483.216.7705
Email: gavin@valtrimsystems-example.com
Website: www.valtrimsystems-example.com

```html
<!DOCTYPE html>
<html lang="en">
<head>
<meta charset="utf-8">
<title>Valtrim Systems – Business Card</title>
<link href="https://fonts.googleapis.com/css2?family=Montserrat:wght@400;600;700&display=swap" rel="stylesheet">
<style>
  :root{
    --backdrop:#b3b3b3;
    --card:#ffffff;
    --brand-blue:#3671ae;
    --ink:#111111;
    --ink-soft:#3a3a3a;
    --contact-ink:#1f2330;
  }
  *{margin:0;padding:0;box-sizing:border-box;}
  html,body{width:1200px;height:1127px;overflow:hidden;}
  body{background:var(--backdrop);font-family:'Montserrat',sans-serif;position:relative;}

  .card{position:absolute;left:297px;width:607px;height:347px;background:var(--card);}
  .card--front{top:141px;}
  .card--back{top:623px;}

  .wordmark{font-family:'Montserrat',sans-serif;font-weight:700;color:var(--ink);
    letter-spacing:.04em;white-space:nowrap;position:absolute;}
  .card--front .wordmark{font-size:36px;left:0;right:0;top:150px;text-align:center;}
  .card--back .wordmark{font-size:19px;left:32px;width:220px;top:160px;text-align:center;}

  .fold{position:absolute;left:285px;top:82px;width:20px;height:184px;}

  .identity{position:absolute;left:340px;top:96px;}
  .identity__name{font-size:28px;font-weight:600;color:var(--brand-blue);letter-spacing:.01em;line-height:1;}
  .identity__title{font-size:15.5px;font-weight:400;color:var(--ink-soft);margin-top:3px;letter-spacing:.02em;}

  .contacts{position:absolute;left:341px;top:180px;list-style:none;}
  .contacts__item{display:flex;align-items:center;height:26px;font-size:12px;font-weight:600;color:var(--contact-ink);letter-spacing:.02em;}
  .contacts__icon{width:16px;height:16px;margin-right:14px;flex:none;}

  .accent-band{position:absolute;left:0;right:0;top:316px;height:19px;background:var(--brand-blue);}
</style>
</head>
<body>

<section class="card card--front">
  <div class="wordmark">VALTRIM SYSTEMS</div>
</section>

<section class="card card--back">
  <div class="wordmark">VALTRIM SYSTEMS</div>

  <svg class="fold" viewBox="0 0 20 184" aria-hidden="true">
    <defs>
      <linearGradient id="foldShade" x1="0" x2="1">
        <stop offset="0" stop-color="#cfcfcf"/>
        <stop offset="1" stop-color="#ffffff"/>
      </linearGradient>
    </defs>
    <polygon points="0,0 20,18 20,166 0,184" fill="url(#foldShade)"/>
  </svg>

  <div class="identity">
    <h1 class="identity__name">GAVIN TRELOWE</h1>
    <p class="identity__title">VP Sales / Operations</p>
  </div>

  <ul class="contacts">
    <li class="contacts__item">
      <svg class="contacts__icon" viewBox="0 0 16 16" aria-hidden="true">
        <circle cx="8" cy="8" r="8" fill="var(--brand-blue)"/>
        <path d="M5.2 4.3l1.4-.3.8 1.9-.9.7a5 5 0 0 0 2.4 2.4l.7-.9 1.9.8-.3 1.4c-3.6.3-6.3-2.4-6-6z" fill="#fff"/>
      </svg>
      483.216.7705
    </li>
    <li class="contacts__item">
      <svg class="contacts__icon" viewBox="0 0 16 16" aria-hidden="true">
        <circle cx="8" cy="8" r="8" fill="var(--brand-blue)"/>
        <rect x="4.2" y="5.3" width="7.6" height="5.4" fill="none" stroke="#fff" stroke-width="1"/>
        <path d="M4.2 5.3L8 8.4l3.8-3.1" fill="none" stroke="#fff" stroke-width="1"/>
      </svg>
      gavin@valtrimsystems-example.com
    </li>
    <li class="contacts__item">
      <svg class="contacts__icon" viewBox="0 0 16 16" aria-hidden="true">
        <circle cx="8" cy="8" r="7" fill="none" stroke="var(--brand-blue)" stroke-width="1.4"/>
        <ellipse cx="8" cy="8" rx="3" ry="7" fill="none" stroke="var(--brand-blue)" stroke-width="1"/>
        <path d="M1 8h14M2.5 4.5h11M2.5 11.5h11" stroke="var(--brand-blue)" stroke-width="1"/>
      </svg>
      www.valtrimsystems-example.com
    </li>
  </ul>

  <div class="accent-band"></div>
</section>

</body>
</html>
```